Business Card for my building company

I would like the card to make a statement, so as soon as you see the card you think "wow nice card' and then read the details on the card its self. Also i would like to be able to put in the detail for the MUST HAVES so please Crete a box that i can alter depending on who in my business needs the cards. Thank you

Target Market(s)

Any one looking to build a house/ townhouse or duplex

Industry/Entity Type

Home Builder

Contact Information for Business Card

I would like the card to have the logo on the card and the must haves

Font styles to use
Sans Serif

Requirements
Must have
• Name
• Phone Number
• Email Address
• Website
• Licence Number
• Abn

```html
<!DOCTYPE html>
<html lang="en">
<head>
<meta charset="utf-8">
<title>Broadland Builders – Business Card</title>
<link rel="stylesheet" href="https://fonts.googleapis.com/css2?family=Open+Sans:wght@400;600;700&display=swap">
<style>
  :root {
    --page-bg: #e9e7e3;
    --card-white: #ffffff;
    --card-black: #0b0b0b;
    --gold: #c9a548;
    --gold-light: #e3c777;
    --gold-dark: #a98a35;
    --ink: #2a2a2a;
    --text-grey: #555555;
    --logo-grey: #d9d9d9;
  }
  * { margin: 0; padding: 0; box-sizing: border-box; }
  html, body {
    width: 1200px; height: 843px; overflow: hidden;
    background: var(--page-bg);
    font-family: "Open Sans", sans-serif;
  }
  .canvas { position: relative; width: 1200px; height: 843px; }

  .card {
    position: absolute;
    width: 540px; height: 309px;
    border-radius: 4px;
    overflow: hidden;
    box-shadow: 0 6px 18px rgba(0,0,0,0.18);
  }

  /* Back of card */
  .card-back {
    left: 40px; top: 140px;
    background: linear-gradient(160deg, #1c1c1c 0%, var(--card-black) 55%, #000 100%);
  }
  .card-back .brand {
    position: absolute; left: 0; right: 0; top: 110px;
    display: flex; justify-content: center; align-items: center; gap: 12px;
  }
  .card-back .brand-mark {
    width: 18px; height: 18px; background: var(--gold);
  }
  .card-back .brand-name {
    font-weight: 700; font-size: 34px; color: var(--logo-grey); letter-spacing: 0.5px;
  }
  .card-back .web {
    position: absolute; left: 0; right: 0; top: 190px;
    text-align: center; color: var(--logo-grey);
    font-size: 13px; letter-spacing: 6px;
  }

  /* Front of card */
  .card-front {
    left: 620px; top: 394px;
    background: var(--card-white);
  }
  .card-front .person-name {
    position: absolute; left: 40px; top: 26px;
    font-size: 21px; font-weight: 700; color: var(--gold);
  }
  .details {
    position: absolute; left: 40px; top: 150px;
    list-style: none; font-size: 15px; color: var(--text-grey);
  }
  .details li { display: flex; align-items: center; gap: 8px; height: 22px; }
  .details .no-icon { padding-left: 0; }
  .details svg { width: 12px; height: 12px; fill: var(--gold); flex: none; }

  .card-front .brand {
    position: absolute; right: 34px; bottom: 46px;
    display: flex; align-items: center; gap: 10px;
  }
  .card-front .brand-mark { width: 16px; height: 16px; background: var(--gold); }
  .card-front .brand-name { font-size: 24px; font-weight: 700; color: var(--ink); }

  .footer-band { position: absolute; left: 0; right: 0; bottom: 0; height: 20px; display: flex; }
  .footer-band .gold {
    width: 62%;
    background: linear-gradient(180deg, var(--gold-light), var(--gold) 55%, var(--gold-dark));
  }
  .footer-band .black { flex: 1; background: var(--card-black); }
</style>
</head>
<body>
<div class="canvas">

  <section class="card card-back" aria-label="Card back">
    <div class="brand">
      <span class="brand-mark"></span>
      <span class="brand-name">Broadland Builders</span>
    </div>
    <p class="web">www.broadland.com</p>
  </section>

  <section class="card card-front" aria-label="Card front">
    <h1 class="person-name">Daniel Hart</h1>

    <ul class="details">
      <li class="no-icon">Abn 7654321</li>
      <li>
        <svg viewBox="0 0 24 24" aria-hidden="true"><path d="M6.6 10.8a15.1 15.1 0 0 0 6.6 6.6l2.2-2.2c.3-.3.7-.4 1-.2 1.1.4 2.3.6 3.6.6.6 0 1 .4 1 1V20c0 .6-.4 1-1 1A17 17 0 0 1 3 4c0-.6.4-1 1-1h3.5c.6 0 1 .4 1 1 0 1.3.2 2.5.6 3.6.1.3 0 .7-.2 1z"/></svg>
        612 555 0148
      </li>
      <li>
        <svg viewBox="0 0 24 24" aria-hidden="true"><path d="M2 5h20v14H2z M2 5l10 8 10-8" fill="var(--gold)"/><path d="M3 6l9 7 9-7" fill="none" stroke="#fff" stroke-width="1.6"/></svg>
        name@broadland.com
      </li>
      <li>
        <svg viewBox="0 0 24 24" aria-hidden="true"><circle cx="12" cy="12" r="10"/><path d="M2 12h20M12 2c3 3 3 17 0 20M12 2c-3 3-3 17 0 20" fill="none" stroke="#fff" stroke-width="1.4"/></svg>
        www.broadland.com
      </li>
    </ul>

    <div class="brand">
      <span class="brand-mark"></span>
      <span class="brand-name">Broadland Builders</span>
    </div>

    <div class="footer-band">
      <div class="gold"></div>
      <div class="black"></div>
    </div>
  </section>

</div>
</body>
</html>
```